Mother's Day and Baby Blessing poster

I need a poster Mother's Day and Baby Blessing ceremony for a Kestrel Moon Harvest Gala at Sydney Coralinda Wharf. There is no specification on the design, however the only require is to present mother and baby. I would like the design to be modern and simple.

Please refer to the past years design (however I hope it to have a different feel to the past) http://kestrelmoongala.com.au/event/details/baby-blessing-ceremony/.

• Date: 7/5/2017 (Sunday)
• Time: 1:30pm (12:30pm registration)
• Venue: Merrivale Green, Coralinda Wharf

```html
<!DOCTYPE html>
<html lang="en">
<head>
<meta charset="utf-8">
<title>Mother's Day &amp; Baby Blessing Ceremony — Kestrel Moon Harvest Gala</title>
<link rel="stylesheet" href="https://fonts.googleapis.com/css2?family=Barlow+Condensed:wght@400;500&family=Barlow:wght@700&family=Dancing+Script:wght@500&display=swap">
<style>
  :root {
    --orange-top: #ff8200;
    --orange-mid: #ff6a0c;
    --orange-bottom: #ff4712;
    --ink-white: #ffffff;
    --rust: rgba(150, 40, 0, 0.6);
    --rust-soft: rgba(170, 50, 0, 0.28);
    --ribbon: #ffffff;
    --gala-red: #e8321c;
    --halo-pink: #f3b6dc;
    --halo-cream: #fbe8c8;
  }
  html, body {
    margin: 0;
    padding: 0;
    overflow: hidden;
  }
  .poster {
    position: relative;
    width: 845px;
    height: 1200px;
    overflow: hidden;
    background: linear-gradient(180deg, var(--orange-top) 0%, var(--orange-mid) 55%, var(--orange-bottom) 100%);
    font-family: "Barlow Condensed", "Arial Narrow", sans-serif;
    color: var(--ink-white);
  }
  .mother-baby-art {
    position: absolute;
    left: 320px;
    top: 296px;
    width: 525px;
    height: 720px;
    border-radius: 48% 40% 30% 45% / 35% 30% 40% 45%;
    background: radial-gradient(ellipse at 45% 35%, var(--rust-soft) 0%, rgba(170, 50, 0, 0.14) 55%, rgba(170, 50, 0, 0) 80%);
  }
  .title {
    position: absolute;
    left: 52px;
    top: 82px;
    margin: 0;
    font-weight: 400;
    font-size: 88px;
    line-height: 104px;
    white-space: nowrap;
  }
  .ampersand {
    position: absolute;
    left: 464px;
    top: 58px;
    font-family: "Dancing Script", cursive;
    font-weight: 500;
    font-size: 140px;
    line-height: 1;
    color: var(--rust);
  }
  .divider {
    position: absolute;
    left: 50px;
    width: 356px;
    border-top: 1px dashed rgba(255, 255, 255, 0.85);
  }
  .divider--top { top: 352px; }
  .divider--bottom { top: 764px; }
  .details { margin: 0; }
  .details .row {
    position: absolute;
    left: 54px;
    display: block;
    white-space: nowrap;
  }
  .details .date {
    top: 392px;
    font-size: 73px;
    line-height: 73px;
  }
  .details .time {
    top: 486px;
    font-size: 73px;
    line-height: 73px;
  }
  .details .registration {
    top: 561px;
    font-size: 46px;
    line-height: 46px;
  }
  .details .venue {
    left: 57px;
    top: 634px;
    font-size: 43px;
    line-height: 43px;
  }
  .details .venue-line2 {
    left: 110px;
    top: 690px;
  }
  .monk-art {
    position: absolute;
    left: 76px;
    top: 876px;
    width: 232px;
    height: 246px;
    border-radius: 50%;
    background: radial-gradient(circle at 50% 45%, var(--halo-cream) 0%, var(--halo-pink) 60%, rgba(243, 182, 220, 0.2) 100%);
  }
  .gala-ribbon {
    position: absolute;
    left: 304px;
    top: 996px;
    width: 476px;
    height: 132px;
  }
  .gala-name {
    position: absolute;
    left: 332px;
    top: 1010px;
    margin: 0;
    font-family: "Barlow", Arial, sans-serif;
    font-weight: 700;
    font-size: 44px;
    line-height: 52px;
    color: var(--gala-red);
  }
</style>
</head>
<body>
<main class="poster">
  <div class="mother-baby-art" role="img" aria-label="Line illustration of a mother holding and kissing her baby"></div>

  <h1 class="title">Mother's Day<br>Baby Blessing ceremony</h1>
  <span class="ampersand" aria-hidden="true">&amp;</span>

  <div class="divider divider--top"></div>

  <p class="details">
    <span class="row date">Date: 7/5/2017</span>
    <span class="row time">Time: 1:30 PM</span>
    <span class="row registration">(12:30pm registration)</span>
    <span class="row venue">Venue: Merrivale Green,</span>
    <span class="row venue venue-line2">Coralinda Wharf</span>
  </p>

  <div class="divider divider--bottom"></div>

  <div class="monk-art" role="img" aria-label="Illustration of a smiling child monk seated on a lotus in front of a mandala halo"></div>

  <svg class="gala-ribbon" viewBox="0 0 476 132" aria-hidden="true">
    <polygon points="0,0 476,0 432,66 476,132 0,132" fill="var(--ribbon)"/>
  </svg>
  <p class="gala-name">Kestrel Moon<br>Harvest Gala</p>
</main>
</body>
</html>
```